Heron Freightlines needs Bussiness cards!

Our new trucking company needs business cards!
We need the same design with two different names and emails, everything else it's the same.
I have included our original logo so we can use it for the design.
Note: the logo to be used is the o e with the buffalo on the right side, next to the letters H and F.

Target Market(s)

Trucking, refrigerated transportation, freight

Industry/Entity Type

Business

Contact Information for Business Card

Card #1:
Marcus Tellwright
marcustellwright@heronfreightlines.example
1-844-555-0193
(956)555-0178
3817 W. Tarrow Ave.
Pharr, TX 78599
www.heronfreightlines.example

Card#2:
Orla Brennick
orla@heronfreightlines.example
1-844-555-0193
(956)555-0178
3817 W. Tarrow Ave.
Pharr, TX 78599
www.heronfreightlines.example

Font styles to use
Sans Serif

Colors
0655a3
ec1f27
ffffff

Requirements
Must have
• our logo
Nice to have
• roads on background,

```html
<!DOCTYPE html>
<html lang="en">
<head>
<meta charset="utf-8">
<title>Heron Freightlines – Business Cards</title>
<link rel="stylesheet" href="https://fonts.googleapis.com/css2?family=Lato:wght@400;700&family=Montserrat:wght@800&display=swap">
<style>
  :root {
    --brand-blue: #0655a3;
    --brand-red: #ec1f27;
    --brand-white: #ffffff;
    --brand-navy: #17325e;
    --backdrop: #e6e7ea;
    --card-shadow: rgba(0, 0, 0, 0.18);
  }
  * { box-sizing: border-box; margin: 0; padding: 0; }
  html, body { width: 1200px; height: 810px; overflow: hidden; }
  body {
    background: var(--backdrop);
    font-family: "Lato", Arial, sans-serif;
    position: relative;
  }
  .card {
    position: absolute;
    width: 520px;
    height: 300px;
    border-radius: 18px;
    overflow: hidden;
    background: var(--brand-white);
    box-shadow: 0 10px 26px var(--card-shadow);
  }
  .card-front { left: 50px; top: 90px; }
  .card-back { left: 630px; top: 420px; }

  .edge-band {
    position: absolute; left: 0; right: 0; bottom: 0;
    height: 8px; background: var(--brand-red);
  }

  .front-decoration {
    position: absolute; left: 0; top: 40px;
    width: 230px; height: 250px;
    background: linear-gradient(135deg, #f3ddd0 0%, #d7e0ec 55%, #e4e9f1 100%);
    border-radius: 0 60% 40% 0;
    opacity: 0.75;
  }

  .wordmark {
    font-family: "Montserrat", Arial, sans-serif;
    font-weight: 800;
    color: var(--brand-navy);
    display: flex; align-items: center; gap: 10px;
    white-space: nowrap;
    line-height: 1.2;
  }
  .wordmark-dot {
    width: 16px; height: 16px; border-radius: 50%;
    background: var(--brand-red);
  }
  .card-front .wordmark {
    position: absolute; left: 175px; top: 110px; font-size: 31px;
  }
  .front-url {
    position: absolute; left: 300px; top: 218px;
    font-size: 13px; font-weight: 700; color: var(--brand-blue);
  }

  .back-wave { position: absolute; inset: 0; }
  .card-back .wordmark {
    position: absolute; right: 40px; top: 22px; font-size: 22px;
  }
  .card-back .wordmark-dot { width: 13px; height: 13px; }
  .holder-name {
    position: absolute; left: 30px; top: 176px;
    font-size: 22px; line-height: 1.2; color: var(--brand-white); font-weight: 400;
  }
  .contact-list {
    position: absolute; left: 30px; top: 212px;
    list-style: none; color: var(--brand-white); font-size: 13px;
  }
  .contact-list li {
    display: flex; align-items: center; gap: 8px; height: 18px;
  }
  .contact-list svg { width: 12px; height: 12px; fill: var(--brand-white); flex: none; }
  .office-address {
    position: absolute; right: 24px; top: 132px;
    text-align: right; color: var(--brand-white);
    font-size: 12.5px; line-height: 1.4; font-style: normal;
  }
</style>
</head>
<body>

<section class="card card-front" aria-label="Business card front">
  <div class="front-decoration" role="img" aria-label="Faint large brand emblem decoration"></div>
  <div class="wordmark"><span class="wordmark-dot"></span>Heron Freightlines</div>
  <p class="front-url">www.heronfreightlines.example</p>
  <div class="edge-band"></div>
</section>

<section class="card card-back" aria-label="Business card back">
  <svg class="back-wave" viewBox="0 0 520 300" preserveAspectRatio="none" aria-hidden="true">
    <path d="M0,172 C120,130 300,130 520,58 L520,300 L0,300 Z" fill="var(--brand-blue)"/>
    <path d="M0,160 C120,118 300,118 520,46" fill="none" stroke="var(--brand-red)" stroke-width="6"/>
    <rect x="0" y="293" width="520" height="7" fill="var(--brand-red)"/>
  </svg>

  <div class="wordmark"><span class="wordmark-dot"></span>Heron Freightlines</div>

  <address class="office-address">3817 W. Tarrow Ave. Pharr<br>TX 78599</address>

  <h1 class="holder-name">Marcus Tellwright</h1>
  <ul class="contact-list">
    <li>
      <svg viewBox="0 0 24 24" aria-hidden="true"><path d="M6.6 10.8a15.1 15.1 0 0 0 6.6 6.6l2.2-2.2a1 1 0 0 1 1-.25 11.4 11.4 0 0 0 3.6.6 1 1 0 0 1 1 1V20a1 1 0 0 1-1 1A17 17 0 0 1 3 4a1 1 0 0 1 1-1h3.5a1 1 0 0 1 1 1c0 1.25.2 2.45.6 3.6a1 1 0 0 1-.25 1z"/></svg>
      1-844-555-0193
    </li>
    <li>
      <svg viewBox="0 0 24 24" aria-hidden="true"><path d="M7 1h10a2 2 0 0 1 2 2v18a2 2 0 0 1-2 2H7a2 2 0 0 1-2-2V3a2 2 0 0 1 2-2zm0 3v14h10V4zm5 15.5a1.2 1.2 0 1 0 0 2.4 1.2 1.2 0 0 0 0-2.4z"/></svg>
      (956)555-0178
    </li>
    <li>
      <svg viewBox="0 0 24 24" aria-hidden="true"><path d="M2 5h20v14H2zm2 2v.5l8 5 8-5V7zm0 2.8V17h16V9.8l-8 5z"/></svg>
      marcustellwright@heronfreightlines.example
    </li>
    <li>
      <svg viewBox="0 0 24 24" aria-hidden="true"><path d="M12 2a10 10 0 1 0 0 20 10 10 0 0 0 0-20zm6.9 6h-3a15.6 15.6 0 0 0-1.3-3.8A8 8 0 0 1 18.9 8zM12 4c.8 1.2 1.5 2.5 1.9 4h-3.8c.4-1.5 1.1-2.8 1.9-4zM4.3 14a8 8 0 0 1 0-4h3.4a16 16 0 0 0 0 4zm.8 2h3a15.6 15.6 0 0 0 1.3 3.8A8 8 0 0 1 5.1 16zm3-8h-3a8 8 0 0 1 4.3-3.8A15.6 15.6 0 0 0 8.1 8zM12 20c-.8-1.2-1.5-2.5-1.9-4h3.8c-.4 1.5-1.1 2.8-1.9 4zm2.3-6H9.7a14.6 14.6 0 0 1 0-4h4.6a14.6 14.6 0 0 1 0 4zm.3 5.8a15.6 15.6 0 0 0 1.3-3.8h3a8 8 0 0 1-4.3 3.8zm1.7-5.8a16 16 0 0 0 0-4h3.4a8 8 0 0 1 0 4z"/></svg>
      www.heronfreightlines.example
    </li>
  </ul>
</section>

</body>
</html>
```